Manufacturing company needs new business card.

I need a unique Business Card that will truly stand out. Nothing too busy. Simple is good, right? Not looking for a standard design either. No cookie cutter layout. I am just looking for something interesting and a bit different. Does't have to completely off the wall crazy, just not your run of the mill business card. Clean and modern with a touch of industrial.

Target Market(s)

Air conditioning industry, Architects, builders.

Industry/Entity Type

Business

Contact Information for Business Card

Details to be included on card are:

Peter Vance
Managing Director

T: 1300 847 519
M: 0428 593 174
W: www.brenvaleworks.com.au
E: peter.vance@brenvaleworks.com.au
A: 58 Harwick Lane, Sydney NSW 2000

Font styles to use
Sans Serif

Colors
0355a3
848484
fbfbfb

Requirements
Must have
• Card design must be landscape.

```html
<!DOCTYPE html>
<html lang="en">
<head>
<meta charset="utf-8">
<title>Brenvale Works – Business Card</title>
<link rel="stylesheet" href="https://fonts.googleapis.com/css2?family=Alegreya:wght@400;500&display=swap">
<style>
  :root {
    --page: #ffffff;
    --navy: #06215e;
    --blue: #0355a3;
    --blue-line: #2150a8;
    --name-blue: #0d4fae;
    --grey: #848484;
    --contact-grey: #8c93a6;
    --paper: #fbfbfb;
  }
  html, body {
    margin: 0;
    width: 1200px;
    height: 1200px;
    overflow: hidden;
    background: var(--page);
  }
  .card {
    position: absolute;
    left: 180px;
    width: 840px;
    height: 480px;
    display: block;
  }
  .card--front { top: 102px; }
  .card--back { top: 616px; }
  .card-text {
    font-family: "Alegreya", Georgia, serif;
  }
  .holder-name, .holder-role {
    fill: var(--name-blue);
    font-size: 31px;
    letter-spacing: 0.5px;
  }
  .contact-line {
    fill: var(--contact-grey);
    font-size: 18px;
  }
  .brand-name {
    fill: var(--blue);
    font-size: 60px;
    font-weight: 500;
  }
</style>
</head>
<body>

<svg class="card card--front card-text" viewBox="0 0 840 480" aria-label="Card front with contact details">
  <rect class="card-bg" width="840" height="480" fill="var(--navy)"/>
  <g class="accent-lines" stroke="var(--grey)" stroke-width="2">
    <line x1="584" y1="146" x2="840" y2="2"/>
    <line x1="664" y1="138" x2="840" y2="40"/>
  </g>
  <g class="accent-lines" stroke="var(--blue)" stroke-width="1.6">
    <line x1="8" y1="318" x2="288" y2="480"/>
    <line x1="16" y1="346" x2="252" y2="480"/>
    <line x1="16" y1="370" x2="208" y2="480"/>
  </g>
  <text class="holder-name" x="44" y="60">Peter Vance</text>
  <text class="holder-role" x="46" y="101">Managing Director</text>
  <g class="name-rules" stroke="var(--blue)" stroke-width="2">
    <line x1="46" y1="113" x2="106" y2="113"/>
    <line x1="46" y1="118" x2="188" y2="118"/>
    <line x1="46" y1="124" x2="314" y2="124"/>
  </g>
  <g class="contact-block">
    <text class="contact-line" x="446" y="339">T: 1300 847 519</text>
    <text class="contact-line" x="446" y="363">M: 0428 593 174</text>
    <text class="contact-line" x="446" y="387">W: www.brenvaleworks.com.au</text>
    <text class="contact-line" x="446" y="411">E: peter.vance@brenvaleworks.com.au</text>
    <text class="contact-line" x="446" y="435">A: 58 Harwick Lane, Sydney NSW 2000</text>
  </g>
</svg>

<svg class="card card--back card-text" viewBox="0 0 840 480" aria-label="Card back with company name">
  <rect class="card-bg" width="840" height="480" fill="var(--paper)"/>
  <g class="accent-lines" stroke="var(--blue-line)" stroke-width="2.5">
    <line x1="566" y1="156" x2="840" y2="2"/>
    <line x1="0" y1="480" x2="258" y2="334"/>
    <line x1="20" y1="480" x2="234" y2="358"/>
    <line x1="470" y1="420" x2="773" y2="420"/>
    <line x1="390" y1="432" x2="674" y2="432"/>
  </g>
  <rect class="brand-square" x="108" y="198" width="90" height="90" rx="6" fill="var(--blue)"/>
  <text class="brand-name" x="240" y="262">Brenvale Works</text>
</svg>

</body>
</html>
```